Wealth Management Business Card

We are a professional services consulting firm that specializes in high net worth individuals over $25,000,000, executives C-suite and above, closely held businesses owners, family offices and highly compensated employees.

Our focus is on risk mitigation and tax efficient strategies. Our clients take their risk on themselves and have a proven track record generating wealth. Our directive is to preserve and protect the wealth they’ve already created.

Our company Harrowgate Advisory is geared around five directives of asset protection:
1) Legal Structuring
2) Leverage & Financing
3) Risk Management - Asset Protection & Insurance, Trustee Work
4) Asset Management & Investing - Under www.qlvhallmere.com
5) Tax Efficient Strategies

Our Company Mark is a Pentagon with a key in the middle. A pentagon is the most efficient defensive structure. Each point of a pentagon is equal distance front every point . Each side provides support to another and works together, which is the key to our clients success.

Our key colors are blue, black and silver.

We ‘re located in the Pacific Northwest with bi coastal and international clients. We have fewer, higher net worth clients and provide exceptional customer service. We do not do social media.

website is www.harrowgatepath.com

Target Market(s)

High End Clients

Contact Information for Business Card

extra thick

Font styles to use
Serif

Requirements
Must have
• Metalic foil for lettering.
Black Background on one side
White Background on the other
Horizontal Format Only
No Rounded corners
Not Marketing sales information on the card.
Nice to have
• imprinted texture on the card
Should not have
• lots of color

```html
<!DOCTYPE html>
<html lang="en">
<head>
<meta charset="UTF-8">
<title>Harrowgate Advisory – Business Card</title>
<link rel="stylesheet" href="https://fonts.googleapis.com/css2?family=Cinzel:wght@600&family=Poppins:wght@300;400&display=swap">
<style>
  :root {
    --backdrop: #3a3f47;
    --card-white: #f4f5f7;
    --card-black: #0d0d0e;
    --brand-blue: #1a3a8c;
    --deep-blue: #0e2a6e;
    --sky-blue: #1f7fd0;
    --silver: #c9cbcf;
    --silver-dim: #9a9ca0;
    --ink-grey: #5c6068;
  }
  * { box-sizing: border-box; margin: 0; padding: 0; }
  html, body { width: 1200px; height: 900px; overflow: hidden; }
  body {
    background: var(--backdrop);
    position: relative;
    font-family: "Poppins", Arial, sans-serif;
  }
  .card {
    position: absolute;
    width: 560px;
    height: 320px;
    box-shadow: 0 18px 40px rgba(0,0,0,0.45);
  }

  /* Black side */
  .card-back {
    left: 560px;
    top: 100px;
    background: var(--card-black);
    color: var(--silver);
    text-align: center;
    padding-top: 70px;
  }
  .card-back .brand-name {
    font-family: "Cinzel", Georgia, serif;
    font-weight: 600;
    font-size: 34px;
    letter-spacing: 2px;
    color: var(--silver);
  }
  .card-back .divider {
    width: 440px;
    height: 1px;
    margin: 16px auto 18px;
    background: var(--silver-dim);
  }
  .service-list {
    list-style: none;
    font-size: 12.5px;
    font-weight: 300;
    line-height: 1.65;
    color: var(--silver);
  }

  /* White side */
  .card-front {
    left: 90px;
    top: 470px;
    background: var(--card-white);
    overflow: hidden;
    padding: 38px 40px;
  }
  .card-front .brand-name {
    font-family: "Cinzel", Georgia, serif;
    font-weight: 600;
    font-size: 30px;
    letter-spacing: 1.5px;
    color: var(--brand-blue);
  }
  .person-name {
    margin-top: 26px;
    font-family: "Cinzel", Georgia, serif;
    font-weight: 600;
    font-size: 18px;
    letter-spacing: 1px;
    color: var(--brand-blue);
  }
  .contact-list {
    list-style: none;
    margin-top: 14px;
    font-size: 12.5px;
    color: var(--ink-grey);
    line-height: 1.45;
  }
  .contact-list li {
    display: flex;
    align-items: flex-start;
    gap: 9px;
    margin-bottom: 4px;
  }
  .contact-list svg { flex: 0 0 12px; margin-top: 3px; }
  .accent-block {
    position: absolute;
    right: 40px;
    bottom: 40px;
    width: 150px;
    height: 150px;
    background: linear-gradient(135deg, var(--sky-blue), var(--deep-blue));
  }
</style>
</head>
<body>

  <section class="card card-back">
    <h1 class="brand-name">Harrowgate Advisory</h1>
    <div class="divider"></div>
    <ul class="service-list">
      <li>Legal Structuring</li>
      <li>Leverage &amp; Financing</li>
      <li>Risk Management - Asset Protection &amp; Insurance, Trustee Work</li>
      <li>Asset Management &amp; Investing - Under www.qlvhallmere.com</li>
      <li>Tax Efficient Strategies</li>
    </ul>
  </section>

  <section class="card card-front">
    <h1 class="brand-name">Harrowgate Advisory</h1>
    <h2 class="person-name">Corwin Ashdale</h2>
    <ul class="contact-list">
      <li>
        <svg width="12" height="12" viewBox="0 0 12 12" aria-hidden="true"><path d="M2.5 1h2l1 2.5-1.3 1a6 6 0 0 0 3.3 3.3l1-1.3L11 7.5v2A1.5 1.5 0 0 1 9.5 11 8.5 8.5 0 0 1 1 2.5 1.5 1.5 0 0 1 2.5 1z" fill="var(--brand-blue)"/></svg>
        <span>(503) 555-0142</span>
      </li>
      <li>
        <svg width="12" height="12" viewBox="0 0 12 12" aria-hidden="true"><rect x="0.5" y="2" width="11" height="8" fill="var(--brand-blue)"/><path d="M0.5 2.5 6 6.5l5.5-4" stroke="#fff" stroke-width="1" fill="none"/></svg>
        <span>info@harrowgatepath.com</span>
      </li>
      <li>
        <svg width="12" height="12" viewBox="0 0 12 12" aria-hidden="true"><circle cx="6" cy="6" r="5.2" fill="none" stroke="var(--brand-blue)" stroke-width="1.2"/><path d="M0.8 6h10.4M6 0.8c-2.5 3-2.5 7.4 0 10.4M6 0.8c2.5 3 2.5 7.4 0 10.4" stroke="var(--brand-blue)" stroke-width="1" fill="none"/></svg>
        <span>www.harrowgatepath.com</span>
      </li>
      <li>
        <svg width="12" height="12" viewBox="0 0 12 12" aria-hidden="true"><path d="M6 11.5S1.8 7 1.8 4.3a4.2 4.2 0 0 1 8.4 0C10.2 7 6 11.5 6 11.5z" fill="var(--brand-blue)"/><circle cx="6" cy="4.3" r="1.5" fill="#fff"/></svg>
        <span>1184 Alder Ridge Rd, Suite 310,<br>Lake Marlow, OR 97099</span>
      </li>
    </ul>
    <div class="accent-block"></div>
  </section>

</body>
</html>
```